Real Estate Sign 2

Our company is called Corwin Hadley Realty. We are a real estate development company. We need a sign that we are going to hang outside of our projects that says: Another project brought to you by Corwin Hadley Realty... For Sale....(213) 555-0187. At the very bottom is needs to say CaBRE# 04637251" We want the Corwin Hadley Realty to be sophisticated, fresh, simple. We do not have a logo so maybe one can be incorporated into the sign. Sign will be about 30"x24"

Industry/Entity Type

Real Estate

```html
<!DOCTYPE html>
<html lang="en">
<head>
<meta charset="utf-8">
<title>Corwin Hadley Realty – For Sale Sign</title>
<link rel="stylesheet" href="https://fonts.googleapis.com/css2?family=Michroma&family=Orbitron:wght@800&family=Nunito:wght@800&display=swap">
<style>
  :root {
    --brand-red: #d7261f;
    --brand-red-dark: #9e1f1c;
    --brand-blue: #1b3f8f;
    --brand-blue-light: #6fc0ea;
    --ink: #141414;
    --paper: #ffffff;
    --mist: #d9d9d9;
  }
  html, body {
    margin: 0;
    padding: 0;
    width: 1200px;
    height: 959px;
    overflow: hidden;
    background: var(--paper);
  }
  .sign {
    position: relative;
    width: 1200px;
    height: 959px;
    overflow: hidden;
    background: radial-gradient(ellipse 60% 55% at 50% 58%, #ffffff 0%, #f3f3f3 45%, var(--mist) 100%);
  }
  .sign__waves {
    position: absolute;
    inset: 0;
    width: 1200px;
    height: 959px;
  }
  .brand {
    position: absolute;
    left: 56px;
    top: 118px;
    display: flex;
    align-items: center;
    gap: 16px;
    margin: 0;
  }
  .brand__mark {
    width: 40px;
    height: 40px;
    background: var(--ink);
    flex: none;
  }
  .brand__name {
    margin: 0;
    font-family: "Michroma", sans-serif;
    font-weight: 400;
    font-size: 22px;
    line-height: 40px;
    letter-spacing: 0.04em;
    color: var(--ink);
    white-space: nowrap;
  }
  .tagline {
    position: absolute;
    right: 100px;
    top: 278px;
    margin: 0;
    text-align: right;
    font-family: "Michroma", sans-serif;
    font-size: 34px;
    line-height: 53px;
    letter-spacing: 0.22em;
    margin-right: -0.22em;
    color: var(--ink);
    -webkit-text-stroke: 0.7px var(--ink);
    font-variant: small-caps;
    white-space: nowrap;
  }
  .offer {
    position: absolute;
    left: 0;
    top: 520px;
    width: 1200px;
    margin: 0;
    text-align: center;
    font-family: "Orbitron", sans-serif;
    font-weight: 800;
    color: var(--brand-blue);
    text-shadow:
      2px 0 0 #fff, -2px 0 0 #fff, 0 2px 0 #fff, 0 -2px 0 #fff,
      2px 2px 0 #fff, -2px -2px 0 #fff, 2px -2px 0 #fff, -2px 2px 0 #fff,
      2px 4px 4px rgba(0,0,0,0.35);
    white-space: nowrap;
  }
  .offer__status {
    display: block;
    font-size: 68px;
    line-height: 80px;
    letter-spacing: 0.16em;
    font-variant: small-caps;
    margin-left: -30px;
  }
  .offer__phone {
    display: block;
    font-size: 72px;
    line-height: 88px;
    letter-spacing: 0.26em;
    margin-left: 18px;
  }
  .licence {
    position: absolute;
    right: 112px;
    top: 850px;
    margin: 0;
    font-family: "Nunito", sans-serif;
    font-weight: 800;
    font-size: 49px;
    line-height: 60px;
    color: var(--paper);
    text-shadow: 1px 2px 2px rgba(0,0,0,0.35);
    white-space: nowrap;
  }
</style>
</head>
<body>
<main class="sign">
  <svg class="sign__waves" viewBox="0 0 1200 959" aria-hidden="true">
    <defs>
      <linearGradient id="blue-sweep" x1="0" y1="0" x2="1" y2="0">
        <stop offset="0" stop-color="#1b3f8f"/>
        <stop offset="0.5" stop-color="#6fc0ea"/>
        <stop offset="1" stop-color="#1b3f8f"/>
      </linearGradient>
      <linearGradient id="red-sweep" x1="0" y1="0" x2="1" y2="0">
        <stop offset="0" stop-color="#b31f1b"/>
        <stop offset="0.4" stop-color="#e02a22"/>
        <stop offset="1" stop-color="#a11e1b"/>
      </linearGradient>
      <linearGradient id="red-base" x1="0" y1="0" x2="1" y2="0">
        <stop offset="0" stop-color="#9e1f1c"/>
        <stop offset="0.35" stop-color="#d7261f"/>
        <stop offset="1" stop-color="#db2a20"/>
      </linearGradient>
    </defs>

    <path class="wave wave--top-field" fill="#ffffff"
      d="M0,0 H1200 V235 C1050,160 850,165 700,195 C500,240 350,300 230,300 C130,300 50,262 0,220 Z"/>
    <path class="wave wave--top-red" fill="url(#red-sweep)"
      d="M0,220 C50,262 130,300 230,300 C420,300 620,185 860,180 C620,205 430,322 230,320 C120,318 50,300 0,292 Z"/>
    <path class="wave wave--top-blue" fill="url(#blue-sweep)"
      d="M225,303 C450,285 650,172 900,170 C1050,170 1150,215 1200,245 V272 C1120,228 1040,200 900,196 C700,192 500,272 225,303 Z"/>

    <path class="wave wave--bottom-shade" fill="#9e1f1c"
      d="M0,812 C150,830 300,860 460,862 C300,872 150,876 0,880 Z"/>
    <path class="wave wave--bottom-blue" fill="url(#blue-sweep)"
      d="M220,862 C450,842 650,772 850,772 C1000,774 1120,806 1200,822 V842 C1110,815 1000,790 850,790 C650,794 450,852 220,862 Z"/>
    <path class="wave wave--bottom-red" fill="url(#red-base)"
      d="M0,880 C150,868 350,870 520,860 C720,846 900,798 1200,842 V959 H0 Z"/>
    <path class="wave wave--bottom-rule" fill="none" stroke="#ffffff" stroke-width="3"
      d="M0,878 C150,866 350,868 520,858 C720,844 900,796 1200,840"/>
  </svg>

  <div class="brand">
    <span class="brand__mark" aria-hidden="true"></span>
    <h1 class="brand__name">Corwin Hadley Realty</h1>
  </div>

  <p class="tagline">Another project<br>brought to you by<br>Corwin Hadley Realty...</p>

  <p class="offer">
    <span class="offer__status">For Sale</span>
    <span class="offer__phone">(213) 555-0187</span>
  </p>

  <p class="licence">CaBRE# 04637251</p>
</main>
</body>
</html>
```